Business Card for new Architectural Firm

I intend to practice in a rural mountain community in upstate NY, focusing on residential and light commercial projects, including second home / vacation properties. I wish to convey a feeling of rural outdoorsy modernity.

Color is important - bold and urbane. Secondary or tertiary colors preferred.

Font is important, idiosyncratic is ok

Optionally, I may choose to use the name Brackenfold Studio. If used as part of your design, all of the Must Haves are still required.

Images uploaded are logos I like

Industry/Entity Type

Residential

Contact Information for Business Card

Caldwell Prusinski
Architect (This word should stand alone or be associated with my name - not license number)
NY License No. 582163
caldwell@designcpx.com
607 394 2858

Font styles to use
Sans Serif
Decorative

Requirements
Must have
• Whatever files I need to best utilize your design
• PDF
• JPG
• EPS
• Vectorwhatsit
Nice to have
• Logo or element that can be incorporated into other print material.
• Could be a font based card
Should not have
• no clip art
• No templates
• no floor plans
• no building photographs

```html
<!DOCTYPE html>
<html lang="en">
<head>
<meta charset="utf-8">
<title>Brackenfold Studio — Business Card</title>
<link rel="stylesheet" href="https://fonts.googleapis.com/css2?family=Open+Sans:wght@400;600;800&display=swap">
<style>
  :root {
    --page-bg: #d9d6d0;
    --card-top: #2a2a2a;
    --card-bottom: #0b0b0b;
    --brand-green: #8cc63f;
    --text-white: #f2f2f2;
    --text-soft: #e0e0e0;
    --text-grey: #8a8a8a;
    --divider: #9a9a9a;
  }
  * { box-sizing: border-box; margin: 0; padding: 0; }
  html, body {
    width: 1200px;
    height: 900px;
    overflow: hidden;
    background: var(--page-bg);
    font-family: "Open Sans", Verdana, sans-serif;
  }
  .card {
    position: absolute;
    left: 100px;
    top: 165px;
    width: 1000px;
    height: 570px;
    background: radial-gradient(ellipse at 60% 35%, var(--card-top), var(--card-bottom) 75%);
    box-shadow: 0 14px 34px rgba(0, 0, 0, 0.35);
  }
  .card__divider {
    position: absolute;
    left: 480px;
    top: 0;
    width: 1px;
    height: 100%;
    background: linear-gradient(to bottom, transparent, var(--divider) 20%, var(--divider) 80%, transparent);
  }
  .brand {
    position: absolute;
    left: 60px;
    top: 175px;
    width: 390px;
  }
  .brand__name {
    color: var(--brand-green);
    font-weight: 800;
    text-transform: uppercase;
    line-height: 0.95;
    letter-spacing: -1px;
  }
  .brand__name-line1 { display: block; font-size: 54px; }
  .brand__name-line2 { display: block; font-size: 96px; }
  .brand__tagline {
    margin-top: 8px;
    color: var(--text-grey);
    font-size: 21px;
    font-weight: 400;
    letter-spacing: 0.5px;
    text-transform: uppercase;
    white-space: nowrap;
  }
  .contact {
    position: absolute;
    left: 545px;
    top: 130px;
  }
  .contact__name {
    color: var(--text-white);
    font-size: 38px;
    font-weight: 600;
    line-height: 1.15;
  }
  .contact__line {
    color: var(--text-soft);
    font-size: 24px;
    line-height: 1.3;
    padding-left: 14px;
  }
  .license {
    position: absolute;
    right: 40px;
    bottom: 30px;
    color: var(--text-soft);
    font-size: 20px;
  }
</style>
</head>
<body>
  <div class="card">
    <div class="brand">
      <div class="brand__name">
        <span class="brand__name-line1">Brackenfold</span>
        <span class="brand__name-line2">Studio</span>
      </div>
      <div class="brand__tagline">Caldwell Prusinski Architect</div>
    </div>

    <div class="card__divider"></div>

    <div class="contact">
      <div class="contact__name">Caldwell Prusinski</div>
      <div class="contact__line">caldwell@designcpx.com</div>
      <div class="contact__line">607 394 2858</div>
    </div>

    <div class="license">NY License No. 582163</div>
  </div>
</body>
</html>
```